Become a Mentor - For Musicians, Artists, Producers and Teachers

Here is the full creative brief:

https://sheets.quarnelpad.com/file/d/7kTmRwQpZ_3LcN8bJ2HsX5vD4FnYgA9eWu0iPoKqtrr/view?mode=shared

Here is the background image file: https://www.vellicrate.com/sh/48tbnwqzd7kpm3f/AAJx2h8QPW5LuTkZZ-bn4RXCo?dl=0

LOGO:
https://www.vellicrate.com/sh/k273mrtjuz6c8w1/AAHLQ5PrTB9Y-vNJZcKsWp0Ue?dl=0

```html
<!DOCTYPE html>
<html lang="en">
<head>
<meta charset="utf-8">
<title>Start Your Career Today – Become a Mentor</title>
<link rel="stylesheet" href="https://fonts.googleapis.com/css2?family=Archivo+Black&family=Archivo:wght@400;700&family=Open+Sans:wght@400&display=swap">
<style>
  :root {
    --purple-base: #4b2f8e;
    --purple-deep: #35258a;
    --purple-mid: #52368f;
    --purple-light: #7d4aa6;
    --purple-soft: #6a48a0;
    --ink-white: #ffffff;
    --line-white: rgba(255,255,255,0.75);
    --photo-dark: #2a2230;
    --photo-mid: #6b6266;
    --photo-light: #a59d9c;
  }
  * { margin: 0; padding: 0; box-sizing: border-box; }
  html, body { width: 782px; height: 1200px; overflow: hidden; background: var(--purple-base); }
  .poster {
    position: relative;
    width: 782px;
    height: 1200px;
    overflow: hidden;
    background: var(--purple-base);
    color: var(--ink-white);
  }
  .poster__shapes { position: absolute; inset: 0; width: 782px; height: 1200px; }
  .headline {
    position: absolute;
    left: 231px;
    top: 104px;
    font-family: "Archivo Black", "Arial Black", sans-serif;
    line-height: 1;
  }
  .headline__kicker { display: block; font-size: 40px; letter-spacing: 1.5px; }
  .headline__main { display: block; font-size: 90px; letter-spacing: 1px; margin-top: -2px; }
  .headline__sub {
    display: block;
    font-family: "Archivo", Arial, sans-serif;
    font-weight: 400;
    font-size: 38px;
    letter-spacing: -0.5px;
    margin-top: 4px;
  }
  .pitch {
    position: absolute;
    left: 37px;
    top: 862px;
    font-family: "Archivo", Arial, sans-serif;
    font-size: 15.5px;
    line-height: 29px;
    letter-spacing: 0.1px;
    text-transform: uppercase;
  }
  .cta {
    position: absolute;
    left: 37px;
    top: 1028px;
    font-family: "Archivo Black", "Arial Black", sans-serif;
    line-height: 1;
  }
  .cta__action { display: block; font-size: 47px; letter-spacing: 1px; }
  .cta__phone {
    display: block;
    font-family: "Archivo", Arial, sans-serif;
    font-weight: 700;
    font-size: 31px;
    letter-spacing: 1px;
    margin-top: 10px;
  }
  .cta__web {
    position: absolute;
    left: 45px;
    top: 1136px;
    font-family: "Open Sans", Arial, sans-serif;
    font-size: 15px;
    letter-spacing: 0.2px;
  }
  .brand {
    position: absolute;
    left: 490px;
    top: 1080px;
    display: flex;
    align-items: center;
    gap: 10px;
  }
  .brand__dot { width: 34px; height: 34px; border-radius: 50%; background: var(--ink-white); flex: none; }
  .brand__name {
    font-family: "Archivo", Arial, sans-serif;
    font-weight: 700;
    font-size: 21px;
    line-height: 1.1;
    text-transform: uppercase;
    letter-spacing: 0.5px;
    color: var(--ink-white);
  }
</style>
</head>
<body>
<main class="poster">
  <svg class="poster__shapes" viewBox="0 0 782 1200" xmlns="http://www.w3.org/2000/svg">
    <defs>
      <linearGradient id="studio-tones" x1="0" y1="0" x2="1" y2="1">
        <stop offset="0" stop-color="var(--photo-light)"/>
        <stop offset="0.45" stop-color="var(--photo-mid)"/>
        <stop offset="1" stop-color="var(--photo-dark)"/>
      </linearGradient>
      <linearGradient id="lower-wash" x1="0" y1="0" x2="1" y2="1">
        <stop offset="0" stop-color="#5a3d97"/>
        <stop offset="1" stop-color="#7b4aa3"/>
      </linearGradient>
    </defs>

    <!-- background blobs -->
    <ellipse class="shape-blob" cx="130" cy="1260" rx="330" ry="360" fill="var(--purple-soft)" opacity="0.55"/>
    <path class="shape-wave-right" d="M782 395 L782 1200 L540 1200 C600 1000 680 760 782 395 Z" fill="url(#lower-wash)"/>

    <!-- studio photo area -->
    <path class="studio-photo" role="img" aria-label="Photo: two young musicians talking beside a mixing desk and studio monitor in a recording studio"
      d="M0 360 C40 262 90 196 130 176 L782 176 L782 395 C762 430 748 520 705 560 C612 610 560 700 455 830 L0 830 Z"
      fill="url(#studio-tones)"/>

    <!-- right overlay band -->
    <path class="shape-band" d="M774 396 L782 392 L782 600 L774 520 Z" fill="var(--purple-mid)"/>
    <path class="shape-wave-light" d="M782 520 C740 560 700 560 640 600 C590 640 560 720 520 800 L782 800 Z" fill="var(--purple-light)" opacity="0.85"/>

    <!-- large lower circle -->
    <circle class="shape-circle-lower" cx="456" cy="840" r="272" fill="var(--purple-deep)" opacity="0.6"/>

    <!-- large top circle -->
    <circle class="shape-circle-top" cx="486" cy="8" r="272" fill="var(--purple-deep)"/>

    <!-- bottom strip -->
    <rect class="shape-footer-band" x="0" y="1192" width="782" height="8" fill="var(--purple-deep)"/>

    <!-- fine rules -->
    <g class="rules" stroke="var(--line-white)" stroke-width="1">
      <line x1="45" y1="0" x2="45" y2="157"/>
      <line x1="53" y1="0" x2="53" y2="158"/>
      <line x1="62" y1="0" x2="62" y2="173"/>
      <line x1="711" y1="190" x2="711" y2="402"/>
      <line x1="720" y1="205" x2="720" y2="426"/>
      <line x1="728" y1="220" x2="728" y2="432"/>
      <line x1="0" y1="792" x2="64" y2="792"/>
      <line x1="0" y1="797" x2="105" y2="797"/>
      <line x1="525" y1="66" x2="688" y2="66" stroke-opacity="0.3"/>
      <line x1="565" y1="72" x2="688" y2="72" stroke-opacity="0.3"/>
    </g>
  </svg>

  <h1 class="headline">
    <span class="headline__kicker">START YOUR CAREER</span>
    <span class="headline__main">TODAY</span>
    <span class="headline__sub">BECOME A MENTOR</span>
  </h1>

  <p class="pitch">
    Turn your skills and passion for music into a career<br>
    Designed for musicians, artists, producers &amp; teachers
  </p>

  <div class="cta">
    <span class="cta__action">APPLY NOW</span>
    <span class="cta__phone">CALL 1300 482 619</span>
  </div>
  <p class="cta__web">www.meridianschoolofmusic.com.au</p>

  <div class="brand">
    <span class="brand__dot"></span>
    <span class="brand__name">Meridian<br>School of Music</span>
  </div>
</main>
</body>
</html>
```